Wade Merriton Professional Coaching

I would like a website with a mountain theme geared towards professional executives reaching higher peaks and goals. This is a 3 page website with brand essence information on the opening page, the coaching process on a second page and "about me" and lead capture form on a third page

Target Market(s)

C-Level audience, involved in tech, government, manufacturing, and transportation type of corporations

Coding

Number of Pages Required

3 page

Font styles to use
Sans Serif

Colors
a7a7a7
1b1b1b
e8e8e8
3176b5
abd036
0355a3

Requirements
Must have
• Looking for a user friendly site that I can manage/update going forward. Must have:
• 1. "Is coaching right for you?" - page 1
• 2. "Our Process" page 2 - I will describe how we approach coaching
• 3. "Contact us" page 3 where I can capture contact information from potential clients
• 4. Clean and professional with more modern font
• 5. Links to personal social media sites
• 6. Ability to upload/download .pdf documents as resources
• 7. Ability to add on new pages in the future (such as a blog page)
Nice to have
• I want a place to store articles I write or use.
• LinkedIn or Twitter Feed
Should not have
• Not fluffy or too 'zen' like personal life coaches tend to present.

```html
<!DOCTYPE html>
<html lang="en">
<head>
<meta charset="utf-8">
<title>Wade Merriton Professional Coaching</title>
<link rel="stylesheet" href="https://fonts.googleapis.com/css2?family=Roboto:wght@300;400;500;700;900&display=swap">
<style>
:root{
  --blue:#1e8fcf;
  --ink:#1b1b1b;
  --text:#333;
  --muted:#a7a7a7;
  --footer:#2b2b2b;
  --footer-deep:#1b1b1b;
  --white:#fff;
  --arrow:#2f3338;
}
*{margin:0;padding:0;box-sizing:border-box}
html,body{width:1040px;height:1200px;overflow:hidden;background:var(--white);font-family:'Roboto',sans-serif;font-weight:400;color:var(--text)}
.page{position:relative;width:1040px;height:1200px;overflow:hidden}
.top-line{position:absolute;left:0;top:0;width:100%;height:2px;background:var(--blue);z-index:5}
.hero{position:absolute;left:0;top:0;width:1040px;height:504px;
  background:
    radial-gradient(ellipse 560px 230px at 260px 520px,rgba(222,228,233,.95) 0%,rgba(205,214,221,.8) 50%,rgba(205,214,221,0) 100%),
    radial-gradient(ellipse 260px 180px at 470px 500px,rgba(214,221,227,.8) 0%,rgba(214,221,227,0) 100%),
    linear-gradient(180deg,#e2e5e9 0%,#cfd4da 14%,#8c99aa 34%,#66768c 52%,#6f7e92 72%,#8b96a4 100%)}
.brand{position:absolute;left:219px;top:14px;display:flex;align-items:center;gap:6px;font-size:17px;color:#36414c;z-index:6;letter-spacing:.3px}
.brand-mark{width:26px;height:26px;background:var(--blue)}
.nav{position:absolute;top:18px;left:621px;display:flex;align-items:center;gap:14px;font-size:8px;letter-spacing:.6px;color:#3d4650;font-weight:500;z-index:6}
.nav a{color:inherit;text-decoration:none}
.nav .active{background:var(--blue);color:var(--white);padding:5px 9px}
.slide-arrow{position:absolute;top:212px;width:36px;height:36px;background:var(--arrow);display:flex;align-items:center;justify-content:center}
.slide-arrow.prev{left:36px}.slide-arrow.next{left:969px}
.hero-copy{position:absolute;left:0;top:194px;width:1040px;text-align:center;color:var(--white)}
.hero-kicker{font-weight:300;font-size:32px;line-height:36px}
.hero-title{font-weight:900;font-size:48px;line-height:58px;margin-top:2px;text-shadow:0 2px 4px rgba(0,0,0,.35)}
.hero-lede{width:400px;margin:8px auto 0;font-size:11px;line-height:14px;font-weight:300}
.dots{position:absolute;top:476px;left:490px;display:flex;gap:8px}
.dots span{width:15px;height:2px;background:var(--white)}
.dots span.on{background:var(--blue)}
.portrait{position:absolute;left:222px;top:328px;width:262px;height:494px;
  background:linear-gradient(180deg,#4a5d80 0%,#34466b 45%,#252f47 100%)}
.portrait-shadow{position:absolute;left:200px;top:818px;width:380px;height:14px;border-radius:50%;background:radial-gradient(ellipse at center,rgba(0,0,0,.12),rgba(0,0,0,0) 70%)}
.about{position:absolute;left:543px;top:546px;width:278px}
.about h2{font-weight:400;font-size:18px;color:var(--ink);display:flex;align-items:center;gap:7px}
.about h2::after{content:"";width:22px;height:1px;background:#555;margin-top:6px}
.about p{margin-top:15px;font-size:7.5px;line-height:13.5px;color:var(--ink);font-weight:400}
.about ul{list-style:none;margin-top:23px}
.about li{display:flex;align-items:center;gap:12px;font-size:7.5px;color:#555;height:21.6px;font-weight:300}
.about li svg{flex:none}
.footer{position:absolute;left:0;top:879px;width:1040px;height:285px;background:var(--footer)}
.contact-card{position:absolute;top:27px;width:192px;height:48px;border:1px solid var(--blue);display:flex}
.contact-card .icon{width:45px;height:100%;background:var(--blue);display:flex;align-items:center;justify-content:center;flex:none}
.contact-card .info{padding:8px 0 0 8px}
.contact-card .label{font-size:6px;font-weight:500;color:var(--blue);letter-spacing:.4px}
.contact-card .value{margin-top:6px;font-size:7px;line-height:12px;color:var(--white);font-weight:400;letter-spacing:.2px}
.rule{position:absolute;left:220px;top:97px;width:601px;height:1px;background:#454545}
.f-brand{position:absolute;left:220px;top:126px;display:flex;align-items:center;gap:5px;font-size:12px;color:#cfcfcf}
.f-brand .brand-mark{width:18px;height:18px;background:#9a9a9a}
.f-about{position:absolute;left:220px;top:164px;width:195px;font-size:8px;line-height:15.2px;color:var(--muted);letter-spacing:.3px}
.f-head{position:absolute;font-size:9px;font-weight:500;color:var(--blue);letter-spacing:.5px}
.f-head::after{content:"";display:block;width:11px;height:1px;background:var(--blue);margin-top:3px}
.f-links{position:absolute;left:425px;top:154px;list-style:none}
.f-links li{font-size:8px;color:var(--muted);height:15.2px;letter-spacing:.3px}
.f-links li::before{content:"›";margin-right:15px}
.socials{position:absolute;left:426px;top:232px;display:flex;gap:4px}
.socials span{width:14px;height:14px;border:1px solid #9a9a9a;border-radius:2px}
.f-news{position:absolute;left:631px;top:154px;width:180px;font-size:8px;line-height:15.2px;color:var(--muted);letter-spacing:.3px}
.email-field{position:absolute;left:631px;top:203px;width:179px;height:27px;border:1px solid #8a8a8a;border-radius:2px;font-size:7.5px;color:var(--muted);padding:9px 6px;letter-spacing:.3px}
.subscribe{position:absolute;left:631px;top:236px;width:179px;height:26px;background:var(--blue);border-radius:2px;color:var(--white);font-size:7.5px;text-align:center;line-height:26px;letter-spacing:.3px}
.legal{position:absolute;left:0;top:1164px;width:1040px;height:36px;background:var(--footer-deep);color:var(--muted);font-size:7.5px;text-align:center;line-height:38px;letter-spacing:.3px}
</style>
</head>
<body>
<div class="page">
  <div class="top-line"></div>
  <div class="hero" role="img" aria-label="Photo of a climber with poles on a snowy mountain ridge under grey clouds"></div>

  <div class="brand"><span class="brand-mark"></span><span>WADE MERRITON</span></div>
  <nav class="nav">
    <a class="active" href="#">HOME</a>
    <a href="#">COACHING PROCESS</a>
    <a href="#" style="margin-left:10px">ABOUT US</a>
  </nav>

  <div class="slide-arrow prev"><svg width="11" height="11" viewBox="0 0 12 12"><path d="M11 6H2M6 1.5 1.5 6 6 10.5" stroke="#fff" stroke-width="2.2" fill="none"/></svg></div>
  <div class="slide-arrow next"><svg width="11" height="11" viewBox="0 0 12 12"><path d="M1 6h9M6 1.5 10.5 6 6 10.5" stroke="#fff" stroke-width="2.2" fill="none"/></svg></div>

  <div class="hero-copy">
    <div class="hero-kicker">Best Place For</div>
    <div class="hero-title">Professional Coaching</div>
    <p class="hero-lede">Lorem ipsum dolor sit amet, consectetur adipiscing elit. Cras eros erat, placerat a eros at, sollicitudin scelerisque ipsum.</p>
  </div>
  <div class="dots"><span class="on"></span><span></span><span></span></div>

  <div class="portrait" role="img" aria-label="Portrait photo of the coach standing in a navy blazer"></div>
  <div class="portrait-shadow"></div>

  <section class="about">
    <h2>About Us</h2>
    <p>Lorem ipsum dolor sit amet, consectetur adipiscing elit. Cras eros erat, placerat a eros at, sollicitudin scelerisque ipsum. Integer dignissim neque vel elit porttitor sodales. Quisque at sem gravida, gravida libero ut, semper neque. Etiam sed sapien at nibh tincidunt fringilla. Integer fermentum nulla diam. Quisque cursus rutrum dui ut placerat. Sed tempus mi sit amet nibh vestibulum, non vestibulum quam tincidunt.</p>
    <ul>
      <li><svg width="7" height="7" viewBox="0 0 8 8"><circle cx="4" cy="4" r="4" fill="#1e8fcf"/><path d="M3 2.2 4.8 4 3 5.8" stroke="#fff" stroke-width="1.2" fill="none"/></svg>Mauris vel justo a quam sodales tristique ac in nisi.</li>
      <li><svg width="7" height="7" viewBox="0 0 8 8"><circle cx="4" cy="4" r="4" fill="#1e8fcf"/><path d="M3 2.2 4.8 4 3 5.8" stroke="#fff" stroke-width="1.2" fill="none"/></svg>Praesent molestie nulla et ligula egestas sagittis.</li>
      <li><svg width="7" height="7" viewBox="0 0 8 8"><circle cx="4" cy="4" r="4" fill="#1e8fcf"/><path d="M3 2.2 4.8 4 3 5.8" stroke="#fff" stroke-width="1.2" fill="none"/></svg>Maecenas vitae libero sed mi eleifend dictum.</li>
      <li><svg width="7" height="7" viewBox="0 0 8 8"><circle cx="4" cy="4" r="4" fill="#1e8fcf"/><path d="M3 2.2 4.8 4 3 5.8" stroke="#fff" stroke-width="1.2" fill="none"/></svg>Fusce quis diam sed sapien ultricies suscipit.</li>
      <li><svg width="7" height="7" viewBox="0 0 8 8"><circle cx="4" cy="4" r="4" fill="#1e8fcf"/><path d="M3 2.2 4.8 4 3 5.8" stroke="#fff" stroke-width="1.2" fill="none"/></svg>Morbi eu nulla interdum, aliquam nulla sit amet, consectetur neque.</li>
    </ul>
  </section>

  <footer class="footer">
    <div class="contact-card" style="left:220px">
      <div class="icon"><svg width="10" height="14" viewBox="0 0 10 14"><path d="M5 0a5 5 0 0 0-5 5c0 3.6 5 9 5 9s5-5.4 5-9a5 5 0 0 0-5-5z" fill="#fff"/><circle cx="5" cy="5" r="1.8" fill="#1e8fcf"/></svg></div>
      <div class="info"><div class="label">VISIT US:</div><div class="value">Contrary to popular belief,<br>Lorem Ipsum is not simply</div></div>
    </div>
    <div class="contact-card" style="left:424px">
      <div class="icon"><svg width="15" height="11" viewBox="0 0 15 11"><rect width="15" height="11" rx="1" fill="#fff"/><path d="M0.5 1 7.5 6.5 14.5 1" stroke="#1e8fcf" stroke-width="1.3" fill="none"/></svg></div>
      <div class="info"><div class="label">MAIL US AT:</div><div class="value" style="margin-top:9px">info@demo.com</div></div>
    </div>
    <div class="contact-card" style="left:629px">
      <div class="icon"><svg width="14" height="14" viewBox="0 0 14 14"><path d="M3 1.5 5 4 3.8 5.5c.8 1.8 2 3 3.8 3.9L9 8.2l2.5 2-1.2 2C6 11.8 2.5 8.3 1.5 3.5z" fill="#fff"/><path d="M8.5 2.5a3 3 0 0 1 3 3M9 0.5a5 5 0 0 1 4.5 4.5" stroke="#fff" stroke-width="1" fill="none"/></svg></div>
      <div class="info"><div class="label">CALL US AT:</div><div class="value">999-999-9999<br>999-999-9999</div></div>
    </div>
    <div class="rule"></div>

    <div class="f-brand"><span class="brand-mark"></span><span>WADE MERRITON</span></div>
    <p class="f-about">Lorem ipsum dolor sit amet, consectetur adipiscing elit. Nullam dolor nulla, pulvinar a risus eu, malesuada imperdiet dui. Donec quis elit nec nibh imperdiet porta volutpat ut lacus. Duis viverra mi lacinia nisi eleifend, sed molestie ipsum consectetur.</p>

    <div class="f-head" style="left:425px;top:134px">Quick Links</div>
    <ul class="f-links"><li>Home</li><li>Coaching Process</li><li>About us</li></ul>
    <div class="f-head" style="left:425px;top:207px">Follow us on</div>
    <div class="socials"><span></span><span></span><span></span><span></span></div>

    <div class="f-head" style="left:631px;top:134px">Quick Links</div>
    <p class="f-news">Lorem ipsum dolor sit amet, consectetur adipiscing elit. Nullam dolor nulla, pulvinar a risus eu, malesuada imperdiet dui.</p>
    <div class="email-field">Enter your Email</div>
    <div class="subscribe">Subscribe Now</div>
  </footer>
  <div class="legal">© wademerriton.com All right reserved.</div>
</div>
</body>
</html>
```